Redesign wellness clinic website

The project is redesign a wellness clinic http://www.thornleighvitality.example. The new website is to be responsive,clean,bright and a strong call to action which is to book an appointment. The logo will remain the same but the colour scheme on the website should be reflect purple white and green. I want it to be bright and cheerful and the feeling of clarity. The website shouldn't be overloaded with content but more visuals.

Target Market(s)

Anyone that has corporate wellness benefits within the downtown Toronto core. Majority of audience are professional working in Media, Telecommunications and Investments.

Industry/Entity Type

Health And Wellness

Number of Pages Required

5+ page

Font styles to use
Sans Serif

Colors
ffffff
886aae
acd036

Requirements
Must have
• -Strong call to action which is book an appointment like this page https://www.kestrelmotion.example/
• -Services provided icons on the page like https://www.brightpathvitalityhouse.example/
• - Pictures of a good visualizing a fit and healthy life
• - Strong ratings from Quorva, Zintrel, PostMaz, similar to this website http://www.summitbalancehealth.example/our-team-professionals/
• - Bright and clear
Should not have
• -No black and white images (redo our pictures)
• -Dark themes

```html
<!DOCTYPE html>
<html lang="en">
<head>
<meta charset="utf-8">
<title>Thornleigh Vitality Centre</title>
<link href="https://fonts.googleapis.com/css2?family=Marcellus&family=Catamaran:wght@400;600;700&display=swap" rel="stylesheet">
<style>
:root{
  --purple:#886aae;
  --purple-dark:#6f5194;
  --green:#acd036;
  --white:#ffffff;
  --ink:#333333;
  --muted:#777777;
  --line:#bbbbbb;
  --footer:#222222;
  --footer-bar:#1a1a1a;
  --card-dark:#2e2e2e;
  --teal:#5fb3b3;
}
*{box-sizing:border-box;margin:0;padding:0}
html,body{width:1200px;height:2812px;overflow:hidden}
body{font-family:"Catamaran",Arial,sans-serif;color:var(--ink);background:var(--white);position:relative}
.abs{position:absolute}
.serif{font-family:"Marcellus",Georgia,serif;font-weight:400}

/* top bar */
.topbar{position:absolute;top:0;left:0;width:1200px;height:30px;background:#f7f7f7;font-size:11px;color:#555}
.topbar .item{position:absolute;top:8px;display:flex;align-items:center;gap:6px}
/* brand */
.brand{position:absolute;top:40px;left:0;width:1200px;display:flex;justify-content:center;align-items:center;gap:10px}
.brand-dot{width:36px;height:36px;border-radius:50%;background:var(--purple)}
.brand-name{font-size:14px;font-weight:700;color:var(--purple);line-height:1.1}
.brand-sub{font-size:9px;color:var(--muted)}
/* nav */
.nav{position:absolute;top:94px;left:244px;width:712px;height:37px;background:var(--purple);border-radius:4px 4px 0 0;display:flex;align-items:center;padding:0 22px;gap:0}
.nav a{color:var(--white);font-size:11.5px;font-weight:600;text-decoration:none;margin-right:34px}
.nav .search{margin-left:auto}
/* hero */
.hero{position:absolute;top:131px;left:0;width:1200px;height:407px;background:linear-gradient(180deg,#8a8276 0%,#b8a48a 45%,#6e6a64 75%,#a08d74 100%)}
.hero .vline{position:absolute;left:599px;width:2px;background:rgba(255,255,255,.7)}
.hero h1{position:absolute;top:110px;width:1200px;text-align:center;color:var(--white);font-size:37px;line-height:56px}
.btn-light{position:absolute;top:243px;left:524px;width:152px;height:36px;border-radius:18px;background:var(--white);color:var(--ink);font-size:10px;font-weight:700;letter-spacing:.5px;display:flex;align-items:center;justify-content:center}
.hero .arrow{position:absolute;top:188px}
/* section titles */
.sec-title{font-size:22px;color:var(--ink)}
/* services */
.services{position:absolute;top:538px;left:0;width:1200px;height:443px}
.services .sec-title{position:absolute;top:36px;width:1200px;text-align:center}
.service{position:absolute;top:82px;width:170px}
.service h3{font-size:13px;font-weight:700;margin:12px 0 6px;color:var(--ink)}
.service ul{list-style:none}
.service li{font-size:10px;line-height:19px;color:#444;padding-left:12px;position:relative}
.service li:before{content:"";position:absolute;left:0;top:8px;width:4px;height:4px;background:#444}
.dots{position:absolute;top:386px;left:0;width:1200px;display:flex;justify-content:center;gap:18px;align-items:center}
.dots span{width:8px;height:8px;border-radius:50%;background:#c9bedb}
.dots span.on{width:12px;height:12px;background:var(--purple)}
/* mission band */
.mission{position:absolute;top:981px;left:0;width:1200px;height:197px;background:var(--purple);color:var(--white);text-align:center}
.mission p{position:absolute;width:1200px;font-size:14px}
.mission b{font-weight:700}
.mission u{font-weight:600}
/* news */
.news{position:absolute;top:1178px;left:0;width:1200px;height:384px}
.head-row{position:absolute;left:244px;width:712px;display:flex;align-items:center;gap:14px}
.head-row .rule{flex:1;border-top:1px dashed var(--line)}
.head-row .tag{font-size:10px;font-weight:700;letter-spacing:.5px}
.card{position:absolute;top:86px;width:225px;height:249px;border-radius:4px;overflow:hidden}
.card .cap{position:absolute;left:18px;bottom:18px;color:var(--white);font-size:12px;font-weight:700}
.card .more{position:absolute;left:18px;bottom:14px;color:var(--white);font-size:10px}
/* staff */
.staff{position:absolute;top:1562px;left:0;width:1200px;height:454px;background:linear-gradient(180deg,#d9d3c8 0%,#b9b6ae 38%,#7d8a92 60%,#8a7d6c 80%,#6a5f52 100%)}
.staff-card{position:absolute;top:43px;left:244px;width:712px;height:364px;background:var(--white);border-radius:5px}
.person{position:absolute;top:88px;width:180px;text-align:center}
.person .photo{position:relative;width:84px;height:84px;margin:0 auto}
.person .photo .blob{position:absolute;left:6px;top:4px}
.person .photo .pic{position:absolute;left:4px;top:2px;width:72px;height:72px;border-radius:50%;background:linear-gradient(160deg,#cfcfcf,#8e8e8e)}
.person h4{font-size:12px;font-weight:700;margin-top:14px}
.person .role{font-size:9.5px;color:#555;margin-top:4px}
.person .contact{font-size:10px;font-weight:700;color:var(--purple);margin-top:10px;letter-spacing:.3px}
.btn-outline{position:absolute;top:298px;left:300px;width:112px;height:36px;border:1.5px solid var(--ink);border-radius:18px;font-size:10px;font-weight:700;letter-spacing:.5px;display:flex;align-items:center;justify-content:center}
/* contact */
.contact{position:absolute;top:2016px;left:0;width:1200px;height:431px}
.map{position:absolute;left:0;top:0;width:590px;height:431px;background:linear-gradient(135deg,#eeeae2 0%,#f3efe6 40%,#e4e6e8 70%,#d8e7c9 100%)}
.contact-info{position:absolute;left:625px;top:0;width:330px}
.contact-info .sec-title{position:absolute;top:40px;font-size:20px}
.ci{position:absolute;font-size:10.5px;color:#444}
.partner{position:absolute;top:300px;left:0;font-size:20px;font-weight:700;color:#1f4e8c;line-height:1}
.partner small{display:block;font-size:8px;letter-spacing:1px;font-weight:700;margin-top:2px}
/* footer */
.footer{position:absolute;top:2447px;left:0;width:1200px;height:328px;background:var(--footer);color:var(--white)}
.footer .sec-title{position:absolute;color:var(--white);font-size:19px}
.about{position:absolute;left:244px;top:160px;width:180px;font-size:10.5px;line-height:17px}
.badge{position:absolute;left:244px;top:264px;width:64px;height:64px;border-radius:6px;background:#c96a2c}
.badge-text{position:absolute;left:322px;top:268px;width:120px;font-size:8.5px;line-height:13px}
.tweet{position:absolute;left:488px;width:225px;height:92px;background:var(--card-dark);border-radius:3px;font-size:10px}
.tweet .who{position:absolute;left:14px;top:16px;display:flex;gap:8px;align-items:flex-start}
.tweet .who i{width:12px;height:12px;border-radius:50%;background:var(--white);display:block;margin-top:1px}
.tweet .link{position:absolute;left:14px;top:66px}
.tweet .date{position:absolute;right:14px;top:66px;font-weight:700}
.tweet .acts{position:absolute;right:14px;top:16px;display:flex;gap:12px}
.video{position:absolute;left:731px;top:94px;width:225px;height:108px;background:linear-gradient(135deg,#6b6b6b,#3c3c3c);border-radius:3px}
.social{position:absolute;left:731px;top:270px;display:flex;gap:14px;font-size:12px;font-weight:700;align-items:center}
.social span{display:flex;align-items:center;gap:5px}
.social i{width:8px;height:8px;border-radius:50%;background:var(--white);display:block}
.bottom{position:absolute;top:2775px;left:0;width:1200px;height:37px;background:var(--footer-bar);color:#ddd;font-size:9.5px;text-align:center;line-height:37px}
</style>
</head>
<body>

<header class="topbar">
  <div class="item" style="left:244px">
    <svg width="10" height="10" viewBox="0 0 10 10"><path d="M2 1l2 2-1 1.5a6 6 0 0 0 2.5 2.5L7 6l2 2-1.5 1.5C4 9 1 6 .5 2.5z" fill="var(--green)"/></svg>
    416-555-0142
    <svg style="margin-left:14px" width="11" height="8" viewBox="0 0 11 8"><rect x=".5" y=".5" width="10" height="7" fill="none" stroke="var(--green)"/><path d="M.5.5l5 4 5-4" fill="none" stroke="var(--green)"/></svg>
    info@thornleighvitality.example
  </div>
  <div class="item" style="right:244px">
    <svg width="10" height="10" viewBox="0 0 10 10"><rect x=".5" y="1.5" width="9" height="8" fill="none" stroke="var(--green)"/><rect x=".5" y="1.5" width="9" height="2" fill="var(--green)"/></svg>
    Book an Appointment
  </div>
</header>

<div class="brand">
  <div class="brand-dot"></div>
  <div>
    <div class="brand-name">Thornleigh Vitality Centre</div>
    <div class="brand-sub">Call 416-555-0142</div>
  </div>
</div>

<nav class="nav">
  <a>Home</a><a>Fees and Services</a><a>News and Updates</a><a>Our Staff</a><a>Corporate Wellness</a><a>Forms</a><a>Contact</a>
  <svg class="search" width="11" height="11" viewBox="0 0 11 11"><circle cx="4.5" cy="4.5" r="3.5" fill="none" stroke="#fff" stroke-width="1.5"/><path d="M7 7l3.5 3.5" stroke="#fff" stroke-width="1.5"/></svg>
</nav>

<section class="hero" role="img" aria-label="Photo of a woman in sportswear running along a sunlit beach">
  <div class="vline" style="top:34px;height:60px"></div>
  <h1 class="serif">Welcome to Thornleigh<br>Vitality Centre</h1>
  <div class="btn-light">BOOK AN APPOINTMENT</div>
  <div class="vline" style="top:290px;height:80px"></div>
  <svg class="arrow" style="left:62px" width="16" height="30" viewBox="0 0 16 30"><path d="M14 2L2 15l12 13" fill="none" stroke="#fff" stroke-width="3"/></svg>
  <svg class="arrow" style="left:1122px" width="16" height="30" viewBox="0 0 16 30"><path d="M2 2l12 13L2 28" fill="none" stroke="#fff" stroke-width="3"/></svg>
</section>

<section class="services">
  <h2 class="sec-title serif">Our Services</h2>

  <div class="service" style="left:244px">
    <svg width="80" height="78" viewBox="0 0 80 78"><path d="M38 4C58 2 76 22 74 44 72 66 50 76 30 72 10 68 2 50 6 32 9 16 22 5 38 4z" fill="var(--purple)"/><g stroke="#fff" stroke-width="1.6" fill="none"><circle cx="40" cy="40" r="5"/><path d="M40 26v6M40 48v6M26 40h6M48 40h6M30 30l4 4M46 46l4 4M50 30l-4 4M34 46l-4 4"/></g></svg>
    <h3>Chiropractic</h3>
    <ul><li>Adjustment</li><li>Functional Adjustment</li><li>Custom Orthotics and Bracing</li></ul>
  </div>

  <div class="service" style="left:426px">
    <svg width="80" height="78" viewBox="0 0 80 78"><path d="M38 4C58 2 76 22 74 44 72 66 50 76 30 72 10 68 2 50 6 32 9 16 22 5 38 4z" fill="none" stroke="var(--purple)" stroke-width="2"/><path d="M8 30C6 14 20 4 30 6" fill="none" stroke="var(--purple)" stroke-width="10" stroke-linecap="round"/><g stroke="var(--purple)" stroke-width="2" fill="none"><rect x="30" y="34" width="20" height="8" rx="2"/><rect x="24" y="30" width="6" height="16" rx="2"/><rect x="50" y="30" width="6" height="16" rx="2"/></g></svg>
    <h3>Physiotherapy</h3>
    <ul><li>Physiotherapy</li><li>Athletic Therapy</li><li>Custom Orthotics and Bracing</li></ul>
  </div>

  <div class="service" style="left:609px">
    <svg width="80" height="78" viewBox="0 0 80 78"><path d="M38 4C58 2 76 22 74 44 72 66 50 76 30 72 10 68 2 50 6 32 9 16 22 5 38 4z" fill="none" stroke="var(--purple)" stroke-width="2"/><path d="M8 30C6 14 20 4 30 6" fill="none" stroke="var(--purple)" stroke-width="10" stroke-linecap="round"/><path d="M32 52V34M37 52V28M42 52V28M47 52V32M32 52c0 4 4 6 8 6s9-2 10-8l4-8" fill="none" stroke="var(--purple)" stroke-width="2" stroke-linecap="round"/></svg>
    <h3>Active Rehabilitation</h3>
    <ul><li>Personal Training</li><li>Pilates</li><li>Fascial Stretch Therapy</li><li>Alexander Technique</li><li>Qigong</li></ul>
  </div>

  <div class="service" style="left:791px">
    <svg width="80" height="78" viewBox="0 0 80 78"><path d="M38 4C58 2 76 22 74 44 72 66 50 76 30 72 10 68 2 50 6 32 9 16 22 5 38 4z" fill="none" stroke="var(--purple)" stroke-width="2"/><path d="M8 30C6 14 20 4 30 6" fill="none" stroke="var(--purple)" stroke-width="10" stroke-linecap="round"/><g fill="none" stroke="var(--purple)" stroke-width="2"><ellipse cx="40" cy="30" rx="7" ry="4"/><ellipse cx="40" cy="40" rx="11" ry="5"/><ellipse cx="40" cy="51" rx="14" ry="5"/></g></svg>
    <h3>Massage Therapy</h3>
    <ul><li>Swedish Massage</li><li>Hot Stone Massage</li><li>Sports Massage</li><li>Shiatsu Massage</li><li>Pregnancy Massage</li><li>Thai Massage</li><li>Foot Reflexology</li><li>Infant Massage</li></ul>
  </div>

  <div class="dots"><span></span><span class="on"></span><span></span></div>
</section>

<section class="mission">
  <p style="top:40px"><b>Our Centre is committed to helping improve and extend the lives of as many people as</b></p>
  <p style="top:63px"><b>possible in our community.</b></p>
  <p style="top:96px">Come and join our Family and start changing your life today.</p>
  <p style="top:130px">Planning a wellness fair? We can help! Contact us at <u>info@thornleighvitality.example</u> for more details.</p>
</section>

<section class="news">
  <div class="head-row" style="top:38px"><h2 class="sec-title serif">News &amp; Updates</h2><span class="rule"></span><span class="tag">VIEW ALL</span></div>
  <article class="card" style="left:244px;background:linear-gradient(180deg,#cde4ea 0%,#a9cfd8 55%,#5f6b6c 85%,#2d2f2f 100%)" role="img" aria-label="Photo of a woman holding a yoga pose on a pier over calm water">
    <div class="cap" style="bottom:40px">Labour Day Weekend Hours</div>
    <div class="more">View More &nbsp;→</div>
  </article>
  <article class="card" style="left:488px;background:linear-gradient(180deg,#9ebbd3 0%,#c3d3df 40%,#7e98a8 70%,#b7c2c4 100%)" role="img" aria-label="Photo of a woman stretching by a mountain lake">
    <div class="cap">Think Well Program</div>
  </article>
  <article class="card" style="left:731px;background:linear-gradient(180deg,#f1c15a 0%,#dd9a2c 50%,#7a4a15 80%,#2a1a08 100%)" role="img" aria-label="Photo of a woman running at golden sunset">
    <div class="cap">Fast Fascia Facts</div>
  </article>
</section>

<section class="staff" role="img" aria-label="Photo of a person on a wooden pier facing the ocean">
  <div class="staff-card">
    <div class="head-row" style="left:44px;width:668px;top:40px"><h2 class="sec-title serif">Our Staff</h2><span class="rule"></span><span class="tag" style="background:var(--white);padding-right:24px">CHIROPRACTIC</span></div>

    <div class="person" style="left:-10px">
      <div class="photo"><svg class="blob" width="82" height="80" viewBox="0 0 82 80"><path d="M40 2C62 0 82 20 80 42 78 66 56 80 34 76 12 72 0 54 4 32 7 16 22 3 40 2z" fill="var(--purple)"/></svg><div class="pic" role="img" aria-label="Portrait of chiropractor"></div></div>
      <h4>Dr. Adrian Pelt</h4><div class="role">Chiropractor, Director of Clinic</div><div class="contact">CONTACT ME</div>
    </div>
    <div class="person" style="left:172px">
      <div class="photo"><svg class="blob" width="82" height="80" viewBox="0 0 82 80"><path d="M40 2C62 0 82 20 80 42 78 66 56 80 34 76 12 72 0 54 4 32 7 16 22 3 40 2z" fill="var(--purple)"/></svg><div class="pic" role="img" aria-label="Portrait of chiropractor"></div></div>
      <h4>Dr. Marcus Veil</h4><div class="role">Chiropractor</div><div class="contact">CONTACT ME</div>
    </div>
    <div class="person" style="left:356px">
      <div class="photo"><svg class="blob" width="82" height="80" viewBox="0 0 82 80"><path d="M40 2C62 0 82 20 80 42 78 66 56 80 34 76 12 72 0 54 4 32 7 16 22 3 40 2z" fill="var(--purple)"/></svg><div class="pic" role="img" aria-label="Portrait of chiropractor"></div></div>
      <h4>Dr. Owen Lacroix</h4><div class="role">Chiropractor, Functional</div><div class="contact">CONTACT ME</div>
    </div>
    <div class="person" style="left:538px">
      <div class="photo"><svg class="blob" width="82" height="80" viewBox="0 0 82 80"><path d="M40 2C62 0 82 20 80 42 78 66 56 80 34 76 12 72 0 54 4 32 7 16 22 3 40 2z" fill="var(--purple)"/></svg><div class="pic" role="img" aria-label="Portrait of chiropractor"></div></div>
      <h4>Nathan Ormsby</h4><div class="role">Chiropractor, Functional</div><div class="contact">CONTACT ME</div>
    </div>

    <div class="btn-outline">VIEW ALL STAFF</div>
  </div>
</section>

<section class="contact">
  <div class="map" role="img" aria-label="Street map of the clinic neighbourhood with a location pin"></div>
  <div class="contact-info">
    <h2 class="sec-title serif">Contact Us</h2>
    <svg class="abs" style="top:90px" width="9" height="12" viewBox="0 0 9 12"><path d="M4.5 12S0 6.5 0 4.5a4.5 4.5 0 0 1 9 0C9 6.5 4.5 12 4.5 12z" fill="var(--purple)"/><circle cx="4.5" cy="4.5" r="1.6" fill="#fff"/></svg>
    <div class="ci" style="top:110px">48 Larkfield Avenue East, Suite 210 Toronto, Ontario M0A 2K4</div>
    <svg class="abs" style="top:143px" width="10" height="10" viewBox="0 0 10 10"><path d="M2 1l2 2-1 1.5a6 6 0 0 0 2.5 2.5L7 6l2 2-1.5 1.5C4 9 1 6 .5 2.5z" fill="var(--purple)"/></svg>
    <div class="ci" style="top:162px">416-555-0142</div>
    <svg class="abs" style="top:143px;left:167px" width="12" height="10" viewBox="0 0 12 10"><rect x="2" y="0" width="8" height="3" fill="var(--purple)"/><rect x="0" y="3" width="12" height="5" rx="1" fill="var(--purple)"/><rect x="3" y="6" width="6" height="4" fill="var(--purple)"/></svg>
    <div class="ci" style="top:162px;left:167px">416-555-0147</div>
    <svg class="abs" style="top:194px" width="11" height="8" viewBox="0 0 11 8"><rect width="11" height="8" fill="var(--purple)"/><path d="M.5.5l5 4 5-4" fill="none" stroke="#fff"/></svg>
    <div class="ci" style="top:210px">info@thornleighvitality.example</div>
    <h2 class="sec-title serif" style="top:256px">Our Partners</h2>
    <div class="partner">Halden<small>DENTAL CENTRES</small></div>
  </div>
</section>

<footer class="footer">
  <div class="abs" style="left:244px;top:44px;display:flex;align-items:center;gap:8px">
    <div style="width:34px;height:34px;border-radius:50%;background:var(--purple)"></div>
    <div><div style="font-size:12px;font-weight:700;color:var(--purple)">Thornleigh Vitality Centre</div><div style="font-size:8px;color:#bbb">Call 416-555-0142</div></div>
  </div>
  <p class="about" style="top:104px">Established in 1980 the Thornleigh Vitality Centre has become one of Canada's leaders in providing quality care and innovative wellness programs for the community [...]</p>
  <div class="badge" style="top:200px" role="img" aria-label="Ranking badge"></div>
  <p class="badge-text" style="top:206px">Thornleigh Vitality Centre is ranked as a top <b>Wellness Centre in Toronto ON</b><br>Verified by Venquil.example</p>

  <h2 class="sec-title serif" style="left:488px;top:52px">Our Tweets</h2>
  <div class="tweet" style="top:94px">
    <div class="who"><i></i><div><b>Thornleigh Vitality</b><br><span style="font-size:9px">@ThornleighVital</span></div></div>
    <div class="acts"><span>♡</span><span>⇄</span></div>
    <div class="link">tv.example/8qwk6D5Rf</div><div class="date">Aug 30, 2017</div>
  </div>
  <div class="tweet" style="top:200px">
    <div class="who"><i></i><div><b>Thornleigh Vitality</b><br><span style="font-size:9px">@ThornleighVital</span></div></div>
    <div class="acts"><span>♡</span><span>⇄</span></div>
    <div class="link">tv.example/8qwk6D5Rf</div><div class="date">Aug 30, 2017</div>
  </div>

  <h2 class="sec-title serif" style="left:731px;top:52px">Video Review</h2>
  <div class="video" role="img" aria-label="Video thumbnail of a clinic review">
    <svg class="abs" style="left:98px;top:40px" width="28" height="28" viewBox="0 0 28 28"><circle cx="14" cy="14" r="13" fill="none" stroke="#fff" stroke-width="1.5"/><path d="M11 8l9 6-9 6z" fill="#fff"/></svg>
  </div>
  <h2 class="sec-title serif" style="left:731px;top:226px">Social Media</h2>
  <div class="social"><span><i></i>Chirpline</span><span><i></i>Circlr</span></div>
</footer>
<div class="bottom">Copyright 2017. Thornleigh Vitality Centre</div>

</body>
</html>
```